Dr.'s Office Forms

This project is recreating/rebranding standard office forms into Maplecrest Oral and Facial Surgery forms. All forms need to be delivered as vector/eps files.

```html
<!DOCTYPE html>
<html lang="en">
<head>
<meta charset="utf-8">
<title>Vendor Check Request – Maplecrest Oral and Facial Surgery</title>
<link rel="stylesheet" href="https://fonts.googleapis.com/css2?family=Mulish:wght@400;700&family=Cormorant+Garamond:wght@600&display=swap">
<style>
  :root {
    --ink: #231f20;
    --rule: #3a3a3a;
    --frame: #4a4a4a;
    --paper: #ffffff;
    --canvas-edge: #8a8a8a;
  }
  * { box-sizing: border-box; margin: 0; padding: 0; }
  html, body { width: 927px; height: 1200px; overflow: hidden; background: var(--paper); }
  body { font-family: "Mulish", sans-serif; color: var(--ink); }

  .sheet {
    position: relative;
    width: 927px; height: 1200px;
    border: 1px solid var(--canvas-edge);
  }
  .form-frame {
    position: absolute;
    left: 55px; top: 98px;
    width: 819px; height: 1006px;
    border: 1.5px solid var(--frame);
  }

  .brand {
    position: absolute;
    left: 584px; top: 178px;
    display: flex; align-items: center; gap: 10px;
  }
  .brand-mark { width: 36px; height: 36px; border-radius: 50%; background: var(--ink); }
  .brand-name {
    font-family: "Cormorant Garamond", serif;
    font-weight: 600;
    font-size: 22px;
    line-height: 1.05;
    color: var(--ink);
    width: 210px;
  }

  .title-rule {
    position: absolute;
    left: 71px; width: 787px;
    border-top: 1.5px solid var(--rule);
  }
  .form-title {
    position: absolute;
    left: 71px; width: 787px; top: 331px;
    text-align: center;
    font-weight: 700; font-size: 19px; letter-spacing: 0.3px;
  }

  .label {
    position: absolute;
    font-size: 15.5px; line-height: 1;
    white-space: nowrap;
  }
  .fill-line {
    position: absolute;
    border-top: 1px solid var(--rule);
  }
</style>
</head>
<body>
<main class="sheet">
  <div class="form-frame"></div>

  <div class="brand">
    <span class="brand-mark"></span>
    <span class="brand-name">Maplecrest Oral and Facial Surgery</span>
  </div>

  <div class="title-rule" style="top:321px"></div>
  <h1 class="form-title">VENDOR CHECK REQUEST</h1>
  <div class="title-rule" style="top:358px"></div>

  <p class="label" style="left:74px; top:405px">To: Accounting Department</p>
  <p class="label" style="left:72px; top:464px">Please issue check payable to:</p>

  <span class="label" style="left:78px; top:502px">Name</span>
  <span class="fill-line" style="left:131px; width:362px; top:523px"></span>
  <span class="label" style="left:621px; top:507px">Date</span>
  <span class="fill-line" style="left:667px; width:175px; top:523px"></span>

  <span class="label" style="left:78px; top:546px">Street</span>
  <span class="fill-line" style="left:131px; width:362px; top:565px"></span>
  <span class="label" style="left:621px; top:551px">Amount</span>
  <span class="label" style="left:696px; top:551px">$</span>
  <span class="fill-line" style="left:680px; width:162px; top:566px"></span>

  <span class="label" style="left:78px; top:589px">City</span>
  <span class="fill-line" style="left:131px; width:362px; top:607px"></span>

  <span class="label" style="left:78px; top:650px">Purpose</span>
  <span class="fill-line" style="left:146px; width:696px; top:668px"></span>
  <span class="fill-line" style="left:146px; width:696px; top:709px"></span>
  <span class="fill-line" style="left:146px; width:696px; top:751px"></span>

  <span class="label" style="left:80px; top:800px">Charge to</span>
  <span class="fill-line" style="left:160px; width:304px; top:814px"></span>

  <span class="label" style="left:80px; top:862px">Instructions:</span>
  <span class="label" style="left:189px; top:862px">Mail to Payee</span>
  <span class="fill-line" style="left:304px; width:160px; top:877px"></span>
  <span class="label" style="left:493px; top:860px">OR</span>
  <span class="label" style="left:531px; top:860px">Deliver to</span>
  <span class="fill-line" style="left:609px; width:160px; top:877px"></span>

  <span class="label" style="left:80px; top:928px">Requestor Signature</span>
  <span class="fill-line" style="left:246px; width:364px; top:939px"></span>

  <span class="label" style="left:80px; top:971px">Authorized Signature</span>
  <span class="fill-line" style="left:246px; width:364px; top:980px"></span>
</main>
</body>
</html>
```